Postcard Design

Maple Ledger Inc.
Title of service: "Ward Wagon" - mobile scrub uniform store, where we go to nursing homes and employees buy their uniforms through us

Photos to consider: nurses, aides, people who work in nursing homes.

need a postcard design for direct mailing nursing homes to promote our traveling nursing uniform store to nursing homes
Contact details:
Email (will provide email to winner only)
Phone 18004729316

Points of Interest to Mention on Card:
Family-Owned Business, Providing impeccable service since 1975
Large Inventory
Stock includes Halvorn, Pellway Brands, budget brands
Reduced Prices
Will work with your schedule to fit your needs
Designated stock colors for your department staff
Special order items are available
150+ top choices per size (XXS-5XL)

Target Market(s)

Director of nursing, nursing homes staff

Industry/Entity Type

Store

```html
<!DOCTYPE html>
<html lang="en">
<head>
<meta charset="utf-8">
<title>Ward Wagon – Postcard</title>
<link rel="stylesheet" href="https://fonts.googleapis.com/css2?family=Bitter:wght@500&family=Open+Sans:wght@400;600&display=swap">
<style>
  :root {
    --page-bg: #e4e4e4;
    --card-white: #ffffff;
    --ink-black: #0b0b0b;
    --rule-grey: #d9d9d9;
    --teal-dark: #26b899;
    --teal-light: #55c6ab;
    --text-white: #ffffff;
    --bullet-cream: #f3e6cf;
    --photo-blue: #2f86c6;
    --photo-cream: #ede6dc;
    --photo-warm: #d8c6b4;
  }
  * { box-sizing: border-box; margin: 0; padding: 0; }
  html, body {
    width: 1200px; height: 834px; overflow: hidden;
    background: var(--page-bg);
    font-family: "Open Sans", Arial, sans-serif;
  }
  .card-set {
    position: absolute; left: 17px; top: 220px;
    width: 1227px; height: 414px;
    transform: scale(0.95); transform-origin: top left;
  }
  /* ---------- Address side ---------- */
  .card-back {
    position: absolute; left: 0; top: 0;
    width: 597px; height: 413px;
    background: var(--card-white);
    overflow: hidden;
  }
  .card-back .photo {
    position: absolute; left: 0; top: 0; width: 259px; height: 413px;
    background: linear-gradient(100deg, var(--photo-blue) 0%, var(--photo-blue) 38%, var(--photo-cream) 62%, #f6f3ef 100%);
  }
  .title-block { position: absolute; }
  .card-back .title-block { left: 82px; top: 16px; }
  .brand-name {
    display: block; background: var(--ink-black); color: var(--text-white);
    font-family: "Bitter", Georgia, serif; font-weight: 500;
  }
  .card-back .brand-name { width: 189px; height: 45px; font-size: 27px; line-height: 45px; padding-left: 12px; }
  .card-back .tagline {
    display: block; width: 178px; height: 16px; background: var(--card-white);
    font-family: "Bitter", Georgia, serif; font-size: 12.5px; line-height: 16px; color: #222; padding-left: 1px;
  }
  .card-back .tag-fold {
    position: absolute; left: 178px; top: 45px;
    width: 0; height: 0; border-top: 16px solid var(--ink-black); border-right: 11px solid transparent;
  }
  .stamp-box {
    position: absolute; left: 502px; top: 20px; width: 73px; height: 100px;
    border: 2px solid var(--rule-grey); border-radius: 14px;
  }
  .address-line { position: absolute; height: 1.5px; background: var(--rule-grey); right: 22px; }
  /* ---------- Message side ---------- */
  .card-front {
    position: absolute; left: 627px; top: 0;
    width: 600px; height: 414px;
    background: var(--ink-black);
    overflow: hidden;
  }
  .card-front .photo {
    position: absolute; left: 0; top: 46px; width: 600px; height: 262px;
    background: linear-gradient(90deg, #b89c87 0%, var(--photo-warm) 35%, #e9e1d6 55%, var(--photo-blue) 72%, #2a6fb0 100%);
  }
  .pennant { position: absolute; left: 55px; top: 46px; }
  .card-front .title-block { left: 35px; top: 92px; }
  .card-front .brand-name { width: 236px; height: 35px; font-size: 26px; line-height: 35px; padding-left: 34px; }
  .pennant-text {
    position: absolute; left: 55px; width: 196px; text-align: center; color: var(--text-white);
  }
  .service-line { top: 135px; font-size: 12px; }
  .service-detail { top: 156px; font-size: 8.5px; line-height: 12px; }
  .contact-heading { top: 238px; font-size: 8.5px; }
  .contact-phone { top: 252px; font-size: 8.5px; }
  .points {
    position: absolute; top: 330px; list-style: none;
    color: var(--text-white); font-size: 8.6px; line-height: 15.5px;
  }
  .points li { position: relative; padding-left: 18px; }
  .points li::before {
    content: ""; position: absolute; left: 0; top: 5px;
    width: 5px; height: 5px; border-radius: 50%; background: var(--bullet-cream);
  }
  .points-left { left: 12px; }
  .points-right { left: 352px; }
</style>
</head>
<body>
<main class="card-set">
  <section class="card-back" aria-label="Postcard address side">
    <div class="photo" role="img" aria-label="Photo of a nurse in blue scrubs comforting an elderly nursing home resident"></div>
    <div class="title-block">
      <span class="brand-name">Ward Wagon</span>
      <span class="tagline">mobile scrub uniform store</span>
      <span class="tag-fold"></span>
    </div>
    <div class="stamp-box"></div>
    <div class="address-line" style="left:286px; right:112px; top:108px;"></div>
    <div class="address-line" style="left:286px; top:155px;"></div>
    <div class="address-line" style="left:286px; top:202px;"></div>
    <div class="address-line" style="left:286px; top:250px;"></div>
    <div class="address-line" style="left:286px; top:305px;"></div>
    <div class="address-line" style="left:286px; top:360px;"></div>
  </section>

  <section class="card-front" aria-label="Postcard message side">
    <div class="photo" role="img" aria-label="Photo of a smiling nurse in blue scrubs with a stethoscope talking to a resident"></div>
    <svg class="pennant" width="196" height="254" viewBox="0 0 196 254" aria-hidden="true">
      <polygon points="0,0 96,0 96,254 0,208" fill="var(--teal-dark)"/>
      <polygon points="96,0 196,0 196,208 96,254" fill="var(--teal-light)"/>
    </svg>
    <div class="title-block">
      <span class="brand-name">Ward Wagon</span>
    </div>
    <p class="pennant-text service-line">mobile scrub uniform store</p>
    <p class="pennant-text service-detail">where we go to nursing homes and<br>employees buy their uniforms through us</p>
    <p class="pennant-text contact-heading">Contact details</p>
    <p class="pennant-text contact-phone">Phone : 18004729316</p>
    <ul class="points points-left">
      <li>Family-Owned Business, Providing impeccable service since 1975</li>
      <li>Stock includes Halvorn, Pellway Brands, budget brands</li>
      <li>Designated stock colors for your department staf</li>
      <li>&nbsp;Will work with your schedule to fit your needs</li>
    </ul>
    <ul class="points points-right">
      <li>150+ top choices per size (XXS-5XL)</li>
      <li>Special order items are available</li>
      <li>Reduced Prices</li>
      <li>Large Inventory</li>
    </ul>
  </section>
</main>
</body>
</html>
```